Lone Ember Barbeque Soss*

Design a branded label for a bottle of sauce..... for LONE EMBER BBQ
FOOD LABEL. Target audience is woman buying bbq sauce for men. There is a lot of competition in the market so Texas should really be a highlight. LOGO SHOULD BE BIG. PLEASE RECREATE IF YOU CAN.

I am looking for a unique die cut....

Target Market(s)

GENERAL GROCERY STORE

Industry/Entity Type

Retail

Colors
f58946
ec1f27
f78f20
fee18a
f48541

Requirements
Must have
• LONE EMBER BBQ SAUCE
Nice to have
• ILLUSTRATIONS
Should not have
• NO PICTURES BUT

```html
<!DOCTYPE html>
<html lang="en">
<head>
<meta charset="utf-8">
<title>Lone Ember BBQ Sauce – Bottle Label</title>
<link rel="stylesheet" href="https://fonts.googleapis.com/css2?family=Bebas+Neue&family=Lato:wght@400;700&family=Roboto+Condensed:wght@400;700&family=Archivo:wght@400;700;900&display=swap">
<style>
  :root {
    --backdrop: #d4d5d7;
    --label-black: #060606;
    --paper: #ffffff;
    --ember-red: #ec1f27;
    --ember-orange: #f58946;
    --ember-amber: #f78f20;
    --ember-gold: #fee18a;
    --ink: #111111;
    --text-light: #ffffff;
  }
  * { margin: 0; padding: 0; box-sizing: border-box; }
  html, body {
    width: 1200px; height: 534px; overflow: hidden;
    background: var(--backdrop);
  }
  .canvas { position: relative; width: 1200px; height: 534px; }

  .label {
    position: absolute; left: 102px; top: 104px; width: 1021px; height: 326px;
    background: var(--label-black);
    box-shadow: 5px 6px 6px rgba(0,0,0,0.35);
  }

  /* left copy panel */
  .copy { position: absolute; left: 127px; color: var(--text-light);
    font-family: 'Lato', sans-serif; }
  .copy-heading { top: 130px; font-size: 14px; font-weight: 400; letter-spacing: 0.2px; }
  .copy-text { width: 291px; font-size: 9.3px; line-height: 11.8px; text-align: justify; }
  .copy-text.first { top: 153px; }
  .copy-text.last { top: 290px; }
  .copy-box {
    position: absolute; left: 127px; top: 229px; width: 292px; height: 51px;
    border: 1.5px solid var(--text-light); padding: 5px 7px;
    color: var(--text-light); font-family: 'Lato', sans-serif;
    font-size: 9.3px; line-height: 11.8px; text-align: justify;
  }
  .dates { position: absolute; left: 268px; color: var(--text-light);
    font-family: 'Lato', sans-serif; font-size: 9.5px; }
  .dates.issue { top: 345px; }
  .dates.expiry { top: 377px; }

  /* centre badge */
  .badge { position: absolute; left: 0; top: 0; }
  .brand-name {
    position: absolute; left: 452px; width: 320px; top: 198px; text-align: center;
    font-family: 'Bebas Neue', sans-serif; font-size: 40px; line-height: 40px;
    color: var(--ink);
  }
  .product-name {
    position: absolute; left: 452px; width: 320px; top: 288px; text-align: center;
    font-family: 'Bebas Neue', sans-serif; font-size: 82px; line-height: 70px;
    color: var(--ink);
  }
  .net-weight {
    position: absolute; left: 452px; width: 320px; top: 366px; text-align: center;
    font-family: 'Lato', sans-serif; font-size: 11.5px; line-height: 14px; color: var(--ink);
  }

  /* certification column */
  .cert { position: absolute; left: 789px; width: 80px; text-align: center; }
  .cert-mark {
    display: block; margin: 0 auto; width: 34px; height: 34px; border-radius: 50%;
    border: 2.5px solid var(--paper);
  }
  .cert-name {
    display: block; margin-top: 6px; color: var(--text-light);
    font-family: 'Roboto Condensed', sans-serif; font-size: 9.5px;
  }
  .cert.gluten { top: 144px; }
  .cert.non-gmo { top: 208px; }
  .cert.halal { top: 274px; }
  .cert.kosher { top: 340px; }

  /* nutrition panel */
  .nutrition {
    position: absolute; left: 878px; top: 130px; width: 209px; height: 274px;
    background: var(--paper); padding: 7px;
  }
  .facts {
    border: 1px solid var(--ink); height: 100%; padding: 2px 3px;
    font-family: 'Archivo', sans-serif; color: var(--ink);
  }
  .facts-title { font-weight: 900; font-size: 20.5px; line-height: 21px; letter-spacing: 1.3px; }
  .facts-serving { font-size: 7.5px; line-height: 9px; border-bottom: 3px solid var(--ink); padding-bottom: 1px; }
  .facts-small { font-size: 5.5px; font-weight: 700; line-height: 8px; border-bottom: 0.5px solid var(--ink); }
  .facts-calories { font-size: 8px; line-height: 11px; border-bottom: 2px solid var(--ink); }
  .facts-dv { font-size: 5.5px; font-weight: 700; text-align: right; line-height: 9px; border-bottom: 0.5px solid var(--ink); }
  .facts-row { display: flex; justify-content: space-between; font-size: 8px; line-height: 11.3px;
    border-bottom: 0.5px solid #999; }
  .facts-row.sub { padding-left: 12px; }
  .facts-row b { font-weight: 700; }
  .facts-row.final { border-bottom: 3px solid var(--ink); }
  .facts-note { font-size: 5px; line-height: 7px; padding-top: 1px; }
  .facts-table { width: 100%; font-size: 5px; line-height: 8.5px; border-collapse: collapse; }
  .facts-table td { padding: 0; }
</style>
</head>
<body>
<div class="canvas">
  <div class="label"></div>

  <h2 class="copy copy-heading">LOREM IPSUM</h2>
  <p class="copy copy-text first">Lorem ipsum dolor sit amet, consectetuer adipiscing elit, sed diam nonummy nibh euismod tincidunt ut laoreet dolore magna aliquam erat volutpat. Ut wisi enim ad minim veniam, quis nostrud exerci tation ullamcorper suscipit lobortis nisl ut aliquip ex ea commodo consequat. Duis autem vel eum iriure dolor.</p>
  <p class="copy-box">Lorem ipsum dolor sit amet, consectetuer adipiscing elit, sed diam nonummy nibh euismod tincidunt ut laoreet dolore magna aliquam erat volutpat. Ut wisi enim ad minim veniam.</p>
  <p class="copy copy-text last">Lorem ipsum dolor sit amet, consectetuer adipiscing elit, sed diam nonummy nibh euismod tincidunt ut laoreet dolore magna aliquam erat volutpat. Ut wisi enim ad minim veniam</p>
  <p class="dates issue">Issue Date:</p>
  <p class="dates expiry">Exp Date:</p>

  <svg class="badge" width="1200" height="534" viewBox="0 0 1200 534" aria-hidden="true">
    <defs>
      <clipPath id="badge-face">
        <polygon points="612,125 753,178 753,356 612,409 471,356 471,178"/>
      </clipPath>
      <linearGradient id="sauce-band" x1="0" y1="0" x2="0" y2="1">
        <stop offset="0" stop-color="var(--ember-red)"/>
        <stop offset="0.5" stop-color="var(--ember-orange)"/>
        <stop offset="1" stop-color="var(--ember-gold)"/>
      </linearGradient>
    </defs>
    <polygon points="612,106 771,167 771,367 612,429 452,367 452,167"
      fill="var(--label-black)" stroke="var(--paper)" stroke-width="3.5" stroke-linejoin="round"/>
    <polygon points="612,125 753,178 753,356 612,409 471,356 471,178"
      fill="var(--paper)" stroke="var(--paper)" stroke-width="6" stroke-linejoin="round"/>
    <rect x="460" y="288" width="305" height="68" fill="url(#sauce-band)" clip-path="url(#badge-face)"/>
  </svg>

  <p class="brand-name">LONE EMBER BBQ</p>
  <h1 class="product-name">BBQ SAUCE</h1>
  <p class="net-weight">Net wt 11 Oz<br>(312g)</p>

  <div class="cert gluten"><span class="cert-mark"></span><span class="cert-name">Gluten Free</span></div>
  <div class="cert non-gmo"><span class="cert-mark"></span><span class="cert-name">Non GMO</span></div>
  <div class="cert halal"><span class="cert-mark"></span><span class="cert-name">Halal Certified</span></div>
  <div class="cert kosher"><span class="cert-mark"></span><span class="cert-name">Kosher Certified</span></div>

  <section class="nutrition">
    <div class="facts">
      <h3 class="facts-title">Nutrition Facts</h3>
      <p class="facts-serving">Serving Size 1 (44g)</p>
      <p class="facts-small">Amount Per Serving</p>
      <p class="facts-calories"><b>Calories</b> 96</p>
      <p class="facts-dv">% Daily Values*</p>
      <p class="facts-row"><span><b>Total Fat</b> 1g</span><b>2%</b></p>
      <p class="facts-row sub"><span>Saturated Fat 0g</span><b>0%</b></p>
      <p class="facts-row sub"><span>Trans Fat 0g</span><span></span></p>
      <p class="facts-row"><span><b>Cholesterol</b> 0mg</span><b>0%</b></p>
      <p class="facts-row"><span><b>Sodium</b> 1mg</span><b>0%</b></p>
      <p class="facts-row"><span><b>Total Carbohydrate</b> 22g</span><b>7%</b></p>
      <p class="facts-row sub"><span>Dietary Fiber 0g</span><b>0%</b></p>
      <p class="facts-row sub"><span>Sugars 6g</span><span></span></p>
      <p class="facts-row final"><span><b>Protein</b> 1g</span><b>2%</b></p>
      <p class="facts-note">*Percent Daily Values are based on a 2,000 calorie diet. Your Daily Values may be higher or lower depending on your calorie needs.</p>
      <table class="facts-table">
        <tr><td></td><td>Calories</td><td>2,000</td><td>2,500</td></tr>
        <tr><td>Total Fat</td><td>Less than</td><td>65g</td><td>80g</td></tr>
        <tr><td>&nbsp;Sat Fat</td><td>Less than</td><td>20g</td><td>25g</td></tr>
        <tr><td>Cholesterol</td><td>Less than</td><td>300mg</td><td>300mg</td></tr>
        <tr><td>Sodium</td><td>Less than</td><td>2400mg</td><td>2400mg</td></tr>
        <tr><td>Total Carbohydrate</td><td></td><td>300g</td><td>375g</td></tr>
        <tr><td>&nbsp;Dietary Fiber</td><td></td><td>25g</td><td>30g</td></tr>
      </table>
    </div>
  </section>
</div>
</body>
</html>
```